New Hand Swiss Brewery needs labels

I need labels for un brand new brewery created in Switzerland called "Brasserie du Galet". The name reflects two things: the air bubbles (CO2) present in beer and the low alcohol level content. I'm brewing a base of 3 types: a refreshing and aromatic american blond, a malty sweet red ale and a German dark wheat beer with character. The beers names are not yet defined but should be on the front mixed up the design. The label should be in one piece with the back containing the information on the ingredients and other informations. The bottles are with à long neck and black (image attached).
Updates

Project Deadline Extended Reason: I still can not decide ... I need a little more proposals or/and improvements !I will reply to messages shortlygreetings and thanks for your work... Added Monday, May 16, 2016

Target Market(s)

Regional

Industry/Entity Type

Brewery

Requirements
Must have
• Ingrédients informations on the back: exemple for the Dark wheat beer
• - IBU (international bitterness unit): 21.9
• - Couleur EBC (color): 36.4
• - Malts: Pilsner, froment, froment caramel, froment grillé, velutto
• - Houblons: Felsora Tundin, Morrowick
• - Levure allemande de fermentation haute
• - Contient: Eau, Malts, houblons, levures
Nice to have
• I like asymmetric style modern graphics. It could be lines and shapes for exemple. Even drawing like comics could be a great idea.

```html
<!DOCTYPE html>
<html lang="fr">
<head>
<meta charset="utf-8">
<title>Brasserie du Galet – American Blond label</title>
<link href="https://fonts.googleapis.com/css2?family=Patrick+Hand+SC&display=swap" rel="stylesheet">
<style>
  :root {
    --page-bg: #ececec;
    --label-red: #d3141b;
    --label-red-deep: #9e0a10;
    --label-red-light: #ef3a3f;
    --ink-white: #ffffff;
    --banner-black: #1b1b1b;
  }
  * { box-sizing: border-box; margin: 0; padding: 0; }
  html, body {
    width: 857px;
    height: 1200px;
    overflow: hidden;
    background: var(--page-bg);
  }
  .label {
    position: absolute;
    left: 128px;
    top: 183px;
    width: 600px;
    height: 833px;
    border: 6px solid var(--ink-white);
    background:
      linear-gradient(90deg,
        var(--label-red-deep) 0%,
        var(--label-red) 18%,
        var(--label-red-light) 38%,
        var(--label-red) 55%,
        var(--label-red-deep) 78%,
        var(--label-red) 100%);
    font-family: "Patrick Hand SC", "Comic Sans MS", cursive;
    color: var(--ink-white);
  }
  .brand-mark {
    position: absolute;
    left: 205px;
    top: 60px;
    width: 180px;
    height: 180px;
  }
  .brand-name {
    position: absolute;
    left: 0;
    top: 340px;
    width: 100%;
    text-align: center;
    font-size: 96px;
    line-height: 96px;
    letter-spacing: 2px;
  }
  .beer-banner {
    position: absolute;
    left: 25px;
    top: 670px;
    width: 500px;
    height: 56px;
  }
  .beer-banner svg { position: absolute; inset: 0; }
  .beer-style {
    position: relative;
    display: block;
    text-align: center;
    font-size: 40px;
    line-height: 56px;
    letter-spacing: 2px;
    color: var(--ink-white);
  }
</style>
</head>
<body>
  <main class="label">
    <svg class="brand-mark" viewBox="0 0 180 180" aria-hidden="true">
      <circle cx="90" cy="90" r="80" fill="none" stroke="var(--ink-white)" stroke-width="8"/>
    </svg>
    <h1 class="brand-name">Brasserie<br>du Galet</h1>
    <div class="beer-banner">
      <svg viewBox="0 0 500 56" preserveAspectRatio="none" aria-hidden="true">
        <polygon points="0,28 18,0 482,0 500,28 482,56 18,56" fill="var(--banner-black)"/>
        <polygon points="10,28 24,6 476,6 490,28 476,50 24,50" fill="none" stroke="var(--ink-white)" stroke-width="2"/>
      </svg>
      <span class="beer-style">American Blond</span>
    </div>
  </main>
</body>
</html>
```